Coralbend Pastoral Traders Business Cards

We require business cards revamped with our logo. A few details we would like to use.

1. Round Edges
2. Our logo over the top of a wagyu cattle background photo on one side of the card

Other side of the card has the below details.

1. Person Name (First & Last)
2. Job Position
3. Mobile Number
4. Email Address
5. Website Address

Simple & Neat.

Target Market(s)

Sales

Industry/Entity Type

Agriculture

Contact Information for Business Card

CORALBEND PASTORAL TRADERS

Colors

Designer to choose colors to be used in the design.

Requirements
Must have
• Company Logo

```html
<!DOCTYPE html>
<html lang="en">
<head>
<meta charset="utf-8">
<title>Coralbend Pastoral Traders Business Cards</title>
<link href="https://fonts.googleapis.com/css2?family=Questrial&display=swap" rel="stylesheet">
<style>
  :root {
    --page: #fdfdfd;
    --card-light: #f3f3f3;
    --maroon: #6e2530;
    --ink: #3b3b3b;
    --ink-soft: #4a4a4a;
    --photo-top: #b58180;
    --photo-mid: #9c5a4f;
    --photo-low: #b06f58;
    --white: #ffffff;
  }
  * { margin: 0; padding: 0; box-sizing: border-box; }
  html, body {
    width: 1200px; height: 1200px; overflow: hidden;
    background: var(--page);
    font-family: "Questrial", sans-serif;
  }
  .canvas { position: relative; width: 1200px; height: 1200px; }

  .card {
    position: absolute; left: 225px; width: 757px; height: 421px;
    border-radius: 40px; overflow: hidden;
  }
  .card--front { top: 159px; }
  .card--back { top: 627px; background: var(--card-light); }

  .cattle-photo {
    position: absolute; inset: 0;
    background:
      radial-gradient(ellipse 45% 55% at 30% 55%, rgba(110,40,35,0.45), transparent 70%),
      radial-gradient(ellipse 35% 45% at 82% 60%, rgba(100,35,35,0.5), transparent 70%),
      linear-gradient(180deg, var(--photo-top) 0%, var(--photo-top) 22%, var(--photo-mid) 50%, var(--photo-low) 100%);
  }

  .brand {
    position: absolute; display: flex; align-items: center; gap: 8px;
    line-height: 1.05; letter-spacing: 0.5px;
  }
  .brand__dot { width: 14px; height: 14px; border-radius: 50%; flex: none; }
  .brand__name { font-size: 19px; text-transform: uppercase; }
  .brand--front { left: 443px; top: 276px; color: var(--white); }
  .brand--front .brand__dot { background: var(--white); }
  .brand--back { left: 114px; top: 186px; color: var(--maroon); }
  .brand--back .brand__dot { background: var(--maroon); }

  .divider {
    position: absolute; left: 378px; top: 61px;
    width: 2px; height: 300px; background: var(--maroon);
  }

  .person { position: absolute; left: 404px; top: 128px; }
  .person__name { font-size: 18.5px; color: var(--ink); font-weight: 700; letter-spacing: 0.2px; }
  .person__role { font-size: 18px; color: var(--ink-soft); margin-top: 2px; }

  .contacts { position: absolute; left: 402px; top: 192px; list-style: none; }
  .contact {
    display: flex; align-items: center; gap: 10px;
    font-size: 18.5px; color: var(--ink-soft); height: 34px;
  }
  .contact svg { width: 16px; height: 16px; flex: none; }
</style>
</head>
<body>
<div class="canvas">

  <section class="card card--front">
    <div class="cattle-photo" role="img" aria-label="Photograph of wagyu cattle standing in tall grass at sunset, tinted in warm rose tones"></div>
    <div class="brand brand--front">
      <span class="brand__dot"></span>
      <span class="brand__name">Coralbend<br>Pastoral Traders</span>
    </div>
  </section>

  <section class="card card--back">
    <div class="brand brand--back">
      <span class="brand__dot"></span>
      <span class="brand__name">Coralbend<br>Pastoral Traders</span>
    </div>

    <div class="divider"></div>

    <div class="person">
      <p class="person__name">First Name Last Name</p>
      <p class="person__role">Job Position</p>
    </div>

    <ul class="contacts">
      <li class="contact">
        <svg viewBox="0 0 24 24" fill="none" stroke="#3b3b3b" stroke-width="1.6" stroke-linecap="round" stroke-linejoin="round"><path d="M5 3h4l2 5-2.5 1.5a11 11 0 0 0 6 6L16 13l5 2v4a2 2 0 0 1-2 2A16 16 0 0 1 3 5a2 2 0 0 1 2-2"/><path d="M15 3a6 6 0 0 1 6 6"/><path d="M15 7a2 2 0 0 1 2 2"/></svg>
        <span>000.0000.0000</span>
      </li>
      <li class="contact">
        <svg viewBox="0 0 24 24" fill="none" stroke="#3b3b3b" stroke-width="1.6" stroke-linejoin="round"><rect x="2.5" y="5" width="19" height="14" rx="1"/><path d="M3 6l9 7 9-7"/></svg>
        <span>name.name@coralbend.com</span>
      </li>
      <li class="contact">
        <svg viewBox="0 0 24 24" fill="none" stroke="#3b3b3b" stroke-width="1.6"><circle cx="12" cy="12" r="9.5"/><ellipse cx="12" cy="12" rx="4" ry="9.5"/><path d="M2.5 12h19M4 7h16M4 17h16"/></svg>
        <span>coralbend.com</span>
      </li>
    </ul>
  </section>

</div>
</body>
</html>
```